Fun modern label needed for olive oil bottle

I need a label for a boutique handmade olive oil line. It needs to be fun and reflect the smallness of the operation and from rural Australia

The name of the line comes from the fact that I live in rural Australia and the black tar road ends 5 km from my home. The road turns to dusty slippery gravel in summer and wet and slippery gravel mud in winter.
Those of us who live out here say that the best people live PAST THE PADDOCKS.

There are no restrictions on colours but it MUST be fun with clear strong lines.

The label is rectangular with the short sides top and bottom. I shall measure the bottles later today and update the brief for you

Below is an example of the bottles used and there will be 3 different sizes
Updates

I have added a couple of photos to show Australian labels and what is need on them sorry to have left out this crucial information

Industry/Entity Type

Boutique

Requirements
Must have
• Past the Paddocks as name
Some sort of logo

```html
<!DOCTYPE html>
<html lang="en">
<head>
<meta charset="utf-8">
<title>Past the Paddocks – Extra Virgin Olive Oil Label</title>
<link rel="stylesheet" href="https://fonts.googleapis.com/css2?family=Oswald:wght@500&family=Pinyon+Script&family=Cinzel:wght@400&display=swap">
<style>
  :root {
    --backdrop: #1c1c1c;
    --label-black: #050505;
    --label-edge: #2e2e2e;
    --gold: #d9b64a;
    --gold-light: #f3e08a;
    --gold-deep: #9a7a1c;
    --ink-white: #f2f2f2;
  }
  html, body {
    margin: 0;
    padding: 0;
    width: 723px;
    height: 1200px;
    overflow: hidden;
    background: var(--backdrop);
  }
  .canvas {
    position: relative;
    width: 723px;
    height: 1200px;
  }
  .label {
    position: absolute;
    left: 225px;
    top: 60px;
    width: 272px;
    height: 1080px;
    background: var(--label-black);
    box-shadow: 0 0 0 1px var(--label-edge);
    overflow: hidden;
  }
  .brand {
    position: absolute;
    top: 28px;
    left: 0;
    width: 100%;
    display: flex;
    flex-direction: column;
    align-items: center;
  }
  .brand-square {
    width: 62px;
    height: 62px;
    background: var(--gold);
  }
  .brand-name {
    margin-top: 12px;
    font-family: "Oswald", sans-serif;
    font-weight: 500;
    font-size: 15px;
    letter-spacing: 0.5px;
    color: var(--gold);
  }
  .product-info {
    position: absolute;
    top: 168px;
    left: 0;
    width: 100%;
    text-align: center;
    font-family: "Oswald", sans-serif;
    font-weight: 500;
    color: var(--ink-white);
    line-height: 1.3;
  }
  .product-type { font-size: 17px; }
  .origin { font-size: 15px; }
  .vertical-title {
    position: absolute;
    left: calc(137px - 300px);
    top: calc(565px - 75px);
    width: 600px;
    height: 150px;
    transform: rotate(-90deg);
    display: flex;
    flex-direction: column;
    align-items: center;
  }
  .line-name {
    height: 90px;
    line-height: 90px;
    font-family: "Pinyon Script", cursive;
    font-size: 60px;
    color: var(--ink-white);
    white-space: nowrap;
  }
  .tagline-row {
    height: 60px;
    width: 100%;
    display: flex;
    align-items: center;
    justify-content: space-between;
  }
  .double-rule {
    width: 100px;
    height: 6px;
    border-top: 2px solid var(--ink-white);
    border-bottom: 2px solid var(--ink-white);
  }
  .tagline {
    font-family: "Cinzel", serif;
    font-size: 20px;
    letter-spacing: 1px;
    color: var(--ink-white);
    white-space: nowrap;
  }
  .leaf-branch {
    position: absolute;
    left: 16px;
    top: 893px;
    width: 256px;
    height: 180px;
    background: radial-gradient(ellipse at 40% 50%, var(--gold-light) 0%, var(--gold) 45%, var(--gold-deep) 75%, var(--label-black) 100%);
    opacity: 0.85;
  }
</style>
</head>
<body>
  <div class="canvas">
    <div class="label">
      <div class="brand">
        <div class="brand-square"></div>
        <div class="brand-name">PAST THE PADDOCKS</div>
      </div>
      <div class="product-info">
        <div class="product-type">EXTRA VIRGIN OLIVE</div>
        <div class="origin">MADE IN AUSTRALIA</div>
      </div>
      <div class="vertical-title">
        <div class="line-name">Past the Paddocks</div>
        <div class="tagline-row">
          <div class="double-rule"></div>
          <div class="tagline">BOUTIQUE HANDMADE</div>
          <div class="double-rule"></div>
        </div>
      </div>
      <div class="leaf-branch" role="img" aria-label="Gold illustration of a curving olive branch with leaves"></div>
    </div>
  </div>
</body>
</html>
```